Restaurant, Nightclub

It's a Restaurant come nightclub. Our sign Lumen is white letters with blue edging on a black back ground.

Industry/Entity Type

Restaurant

Contact Information for Business Card

Lumen Stevenage Ltd
42 Mill Lane
Stevenage Herts SG2 7PQ

```html
<!DOCTYPE html>
<html lang="en">
<head>
<meta charset="utf-8">
<title>Lumen Stevenage Ltd – Business Card</title>
<link rel="stylesheet" href="https://fonts.googleapis.com/css2?family=Arimo:wght@400;700&display=swap">
<style>
  :root {
    --backdrop: #5b3a30;
    --card-blue: #2eb4e9;
    --card-black: #000000;
    --text-white: #ffffff;
  }
  * { margin: 0; padding: 0; box-sizing: border-box; }
  html, body {
    width: 1200px;
    height: 675px;
    overflow: hidden;
    background: var(--backdrop);
  }
  .canvas {
    position: relative;
    width: 1200px;
    height: 675px;
  }
  .business-card {
    position: absolute;
    left: 93px;
    top: 28px;
    width: 978px;
    height: 614px;
    border-radius: 32px;
    overflow: hidden;
    background: var(--card-black);
    display: flex;
  }
  .brand-panel {
    width: 494px;
    height: 100%;
    background: var(--card-blue);
    display: flex;
    align-items: center;
    justify-content: center;
  }
  .divider-gap {
    width: 6px;
    height: 100%;
    background: var(--card-black);
  }
  .divider-stripe {
    width: 11px;
    height: 100%;
    background: var(--card-blue);
  }
  .brand-name {
    font-family: "Arimo", Arial, sans-serif;
    font-weight: 700;
    font-size: 104px;
    letter-spacing: 2px;
    color: var(--text-white);
    margin-top: 2px;
  }
  .contact-panel {
    flex: 1;
    height: 100%;
    background: var(--card-black);
    color: var(--text-white);
    font-family: "Arimo", Arial, sans-serif;
    text-align: center;
    padding-top: 252px;
  }
  .company-name {
    font-size: 30px;
    font-weight: 400;
    line-height: 36px;
  }
  .address {
    margin-top: 30px;
    font-size: 22px;
    line-height: 31px;
    font-style: normal;
  }
</style>
</head>
<body>
  <div class="canvas">
    <div class="business-card">
      <div class="brand-panel">
        <span class="brand-name">Lumen</span>
      </div>
      <div class="divider-gap"></div>
      <div class="divider-stripe"></div>
      <div class="contact-panel">
        <h1 class="company-name">Lumen Stevenage Ltd</h1>
        <address class="address">
          42 Mill Lane<br>
          Stevenage Herts SG2 7PQ
        </address>
      </div>
    </div>
  </div>
</body>
</html>
```